Flyers

Please refer to the attachment. I have been using this design for quite some time now and looks like the design is not attracting anymore attention.
Would prefer similar/new wording with new design that would work.
Remember these flyers get distributed to letter boxes and usually with lots of other letters, newspapers and etc so if the color or design is not appealing chances are that the flyers might not even be seen.
Recommendation: May be NZ $100 note pics in the back ground would help. A nice picture of Vorano van, Ridgewalker 4wd and Truck would preferred.

With the wordings I would like to may be alter or may be even add some more that we buy only Vans, 4WDs, SUV, Trucks. And we can come to you anywhere.

PLEASE DELETE "we sell car parts"
Good luck.

Note: Phone no needs to be changed to 0800394826 and replace address with NATION WIDE but leave website and email on.

```html
<!DOCTYPE html>
<html lang="en">
<head>
<meta charset="utf-8">
<title>Get Cash Now – Vehicles Wanted Flyer</title>
<link rel="stylesheet" href="https://fonts.googleapis.com/css2?family=Anton&family=Archivo+Black&family=Tinos:wght@700&display=swap">
<style>
  :root {
    --red: #c0080d;
    --red-text: #c4070b;
    --yellow: #f6f218;
    --blue-top: #2a2cf0;
    --blue-deep: #0a0a4a;
    --ink: #111111;
    --paper: #f7f7f7;
    --steel-dark: #3b4450;
    --steel-light: #c9d1d8;
    --sky: #4f8fd6;
    --white: #ffffff;
  }
  * { margin: 0; padding: 0; box-sizing: border-box; }
  html, body { width: 1024px; height: 1200px; overflow: hidden; background: var(--paper); }
  .flyer { position: relative; width: 1024px; height: 1200px; overflow: hidden; background: var(--paper); }

  .top-swoosh { position: absolute; left: 0; top: 0; width: 1024px; height: 82px; }

  .cash-band {
    position: absolute; left: 0; top: 82px; width: 1024px; height: 118px;
    background: var(--red); border-top: 4px solid var(--white);
    display: flex; align-items: center; justify-content: center;
  }
  .cash-band h1 {
    font-family: "Tinos", "Times New Roman", serif; font-weight: 700;
    font-size: 98px; letter-spacing: -1px; color: var(--yellow);
    -webkit-text-stroke: 2px #3a0000;
    text-shadow: 4px 5px 0 #2a0000, 6px 8px 6px rgba(0,0,0,.5);
    transform: scaleY(0.92);
  }

  .wanted {
    position: absolute; left: 0; top: 214px; width: 1024px; text-align: center;
    font-family: "Archivo Black", "Arial Black", sans-serif;
    font-size: 150px; line-height: 1; letter-spacing: -2px;
    transform: scaleX(1.02);
  }
  .wanted svg { display: block; margin: 0 auto; }

  .photo { position: absolute; }
  .photo-van {
    left: 322px; top: 458px; width: 320px; height: 206px; border-radius: 26px 60px 14px 14px;
    background: linear-gradient(180deg, #e9eaec 0%, #d2d5d9 60%, #8e9297 100%);
  }
  .photo-4x4 {
    left: 40px; top: 660px; width: 226px; height: 262px; border-radius: 14px 14px 30px 30px;
    background: linear-gradient(180deg, #d9dcdf 0%, #eef0f1 50%, #55595e 100%);
  }
  .photo-truck {
    left: 678px; top: 762px; width: 300px; height: 242px; border-radius: 10px;
    background: linear-gradient(180deg, #cfd3d7 0%, #e8eaec 55%, #6c7075 100%);
  }

  .types {
    position: absolute; left: 0; width: 1024px; text-align: center;
    font-family: "Anton", "Impact", sans-serif; font-size: 66px; line-height: 1;
    color: var(--ink); text-shadow: 4px 6px 6px rgba(0,0,0,.55);
  }
  .types span { display: inline-block; margin: 0 28px; }
  .types-row1 { top: 388px; }
  .types-row2 { top: 476px; }
  .types-row3 { top: 568px; }

  .conditions {
    position: absolute; left: 150px; top: 690px; width: 740px; text-align: center;
    font-family: "Anton", "Impact", sans-serif; font-size: 50px; line-height: 60px;
    color: var(--red-text); letter-spacing: -0.5px;
    -webkit-text-stroke: 1px #200000;
    text-shadow: 3px 4px 0 #1a0000, 4px 6px 5px rgba(0,0,0,.45);
  }

  .bottom-swoosh { position: absolute; left: 0; top: 950px; width: 1024px; height: 250px; }

  .brand {
    position: absolute; left: 80px; top: 1124px;
    display: flex; align-items: center; gap: 12px;
    font-family: "Tinos", "Times New Roman", serif; font-weight: 700;
    font-size: 28px; color: var(--ink);
  }
  .brand-dot { width: 22px; height: 22px; background: var(--red); }

  .contact {
    position: absolute; left: 560px; top: 1074px; width: 464px; text-align: center;
    font-family: "Tinos", "Times New Roman", serif; font-weight: 700;
    font-size: 26px; line-height: 27px; color: var(--white);
    text-shadow: 2px 2px 0 #000, -1px -1px 0 #000, 1px -1px 0 #000, -1px 1px 0 #000;
    letter-spacing: -0.3px;
  }
</style>
</head>
<body>
<main class="flyer">

  <svg class="top-swoosh" viewBox="0 0 1024 82" preserveAspectRatio="none" aria-hidden="true">
    <defs>
      <linearGradient id="topSteel" x1="0" y1="0" x2="1" y2="1">
        <stop offset="0" stop-color="#4a535d"/>
        <stop offset=".35" stop-color="#c7d0d8"/>
        <stop offset=".6" stop-color="#5f6a75"/>
        <stop offset="1" stop-color="#dfe5ea"/>
      </linearGradient>
    </defs>
    <rect width="1024" height="82" fill="url(#topSteel)"/>
    <path d="M0 30 C300 0 600 70 1024 20 L1024 40 C620 85 300 20 0 55 Z" fill="#ffffff" opacity=".35"/>
    <path d="M0 60 C350 40 700 90 1024 50" stroke="#6fa8e6" stroke-width="3" fill="none" opacity=".6"/>
  </svg>

  <header class="cash-band"><h1>GET CASH NOW!!</h1></header>

  <div class="wanted">
    <svg width="660" height="140" viewBox="0 0 660 140" role="img" aria-label="WANTED">
      <defs>
        <linearGradient id="wantedFill" x1="0" y1="0" x2="0" y2="1">
          <stop offset="0" stop-color="#2d30f4"/>
          <stop offset=".55" stop-color="#1a1aa8"/>
          <stop offset="1" stop-color="#07072e"/>
        </linearGradient>
      </defs>
      <text x="336" y="132" text-anchor="middle" font-family="Archivo Black, Arial Black, sans-serif" font-size="150" fill="#111" opacity=".55" textLength="650" lengthAdjust="spacingAndGlyphs">WANTED</text>
      <text x="330" y="126" text-anchor="middle" font-family="Archivo Black, Arial Black, sans-serif" font-size="150" fill="url(#wantedFill)" stroke="#05051c" stroke-width="3" textLength="650" lengthAdjust="spacingAndGlyphs">WANTED</text>
    </svg>
  </div>

  <div class="photo photo-van" role="img" aria-label="Photo of a white Vorano van"></div>
  <div class="photo photo-4x4" role="img" aria-label="Photo of a white Ridgewalker 4WD with roof rack"></div>
  <div class="photo photo-truck" role="img" aria-label="Photo of a white box truck"></div>

  <div class="types types-row1"><span>• VANS</span><span>• TRUCKS</span><span>• SUV’S</span></div>
  <div class="types types-row2"><span>• 4X4’S</span><span>• BOX TRUCKS</span></div>
  <div class="types types-row3"><span>• UTILITY TRUCKS</span></div>

  <p class="conditions">
    Damaged, Mechanical Issues,<br>
    Unregistered, Crashed,<br>
    No WOF - No Problem<br>
    *WE WILL COME TO YOU
  </p>

  <svg class="bottom-swoosh" viewBox="0 0 1024 250" preserveAspectRatio="none" aria-hidden="true">
    <defs>
      <linearGradient id="bottomSteel" x1="0" y1="0" x2="1" y2="1">
        <stop offset="0" stop-color="#2e3742"/>
        <stop offset=".3" stop-color="#8fa3b6"/>
        <stop offset=".55" stop-color="#3d4a58"/>
        <stop offset=".8" stop-color="#a9bccc"/>
        <stop offset="1" stop-color="#4b5a69"/>
      </linearGradient>
    </defs>
    <path d="M0 40 C250 -10 520 60 760 80 C880 90 960 70 1024 60 L1024 250 L0 250 Z" fill="url(#bottomSteel)"/>
    <path d="M0 40 C250 -10 520 60 760 80 C880 90 960 70 1024 60" stroke="#ffffff" stroke-width="6" fill="none" opacity=".8"/>
    <path d="M0 110 C300 60 600 150 1024 95" stroke="#5fa0e8" stroke-width="5" fill="none" opacity=".7"/>
    <path d="M0 180 C260 130 620 210 1024 150" stroke="#ffffff" stroke-width="3" fill="none" opacity=".4"/>
    <path d="M0 150 C220 110 500 170 1024 120 L1024 250 L0 250 Z" fill="#ffffff" opacity=".12"/>
  </svg>

  <div class="brand"><span class="brand-dot"></span>Summit Vehicle Removals Ltd</div>

  <address class="contact">
    NATION WIDE<br>
    Tel: 0800 394 826 | Fax: 04 555 0192<br>
    Mob: 021 555 318<br>
    info@summitremovals.co.nz
  </address>

</main>
</body>
</html>
```